Thornvales Menu Re-Design

Looking to update this menu.

Word doc of menu instructions is uploaded along with photos.

Please estimate cost for completion and expect at least 2-3 rounds of changes.

Thanks!

```html
<!DOCTYPE html>
<html lang="en">
<head>
<meta charset="utf-8">
<title>Thornvales Menu</title>
<link rel="stylesheet" href="https://fonts.googleapis.com/css2?family=Maven+Pro:wght@400;500&family=Quicksand:wght@300;400&display=swap">
<style>
  :root {
    --paper: #efe9df;
    --paper-edge: #e6dfd3;
    --rule: #3a3330;
    --heading: #9a2b2b;
    --item: #8c1f22;
    --body: #6d645c;
    --price: #a2564e;
    --crop: #b9b3ab;
  }
  html, body { margin: 0; padding: 0; overflow: hidden; }
  body { width: 750px; height: 1200px; background: var(--paper); }
  .menu {
    position: relative; width: 750px; height: 1200px; overflow: hidden;
    background: radial-gradient(ellipse at 50% 40%, #f2ede4 0%, var(--paper) 60%, var(--paper-edge) 100%);
    font-family: "Quicksand", sans-serif; color: var(--body);
  }
  .crop { position: absolute; background: var(--crop); }
  .rule { position: absolute; height: 1px; background: var(--rule); }
  .section-title {
    position: absolute; left: 0; width: 750px; text-align: center; margin: 0;
    font-family: "Quicksand", sans-serif; font-weight: 300; color: var(--heading);
    font-size: 38px; letter-spacing: 1.5px; line-height: 44px;
  }
  .section-note {
    position: absolute; left: 0; width: 750px; text-align: center; margin: 0;
    font-size: 11px; color: var(--price); font-weight: 400; letter-spacing: -0.1px;
  }
  .item { position: absolute; }
  .item h3 {
    margin: 0; font-family: "Maven Pro", sans-serif; font-weight: 400;
    font-size: 17px; line-height: 20px; color: var(--item); white-space: nowrap;
  }
  .item p {
    margin: 0; font-size: 11px; line-height: 14px; font-weight: 400; color: var(--body);
    letter-spacing: -0.25px;
  }
  .line { display: flex; justify-content: space-between; white-space: nowrap; }
  .price { color: var(--price); font-size: 11px; line-height: 14px; letter-spacing: 0; }
  .price.solo { display: block; text-align: right; }
  .options { position: absolute; font-size: 11px; line-height: 14px; color: var(--body); }
  .options div { display: flex; }
  .options .label { width: 82px; }
  .options .price { width: 26px; text-align: right; }
</style>
</head>
<body>
<div class="menu">
  <div class="crop" style="left:14px;top:0;width:1px;height:10px"></div>
  <div class="crop" style="left:726px;top:0;width:1px;height:10px"></div>
  <div class="crop" style="left:14px;top:1190px;width:1px;height:10px"></div>
  <div class="crop" style="left:726px;top:1190px;width:1px;height:10px"></div>
  <div class="crop" style="left:0;top:22px;width:10px;height:1px"></div>
  <div class="crop" style="left:740px;top:22px;width:10px;height:1px"></div>

  <!-- Starters -->
  <div class="rule" style="left:60px;top:64px;width:620px"></div>
  <h2 class="section-title" style="top:80px">STARTERS AND SHARABLES</h2>
  <div class="rule" style="left:60px;top:131px;width:620px"></div>

  <div class="item" style="left:86px;top:146px;width:272px">
    <h3>Artichoke and Spinich Dip</h3>
    <p><span class="line">A blend of marinated artichoke hearts, cream cheese,</span>
    <span class="line">leaf spinach, and sharp parmesan. Accompanied with</span>
    <span class="line"><span>Thornvales bread and dipping veggies.</span><span class="price">8.99</span></span></p>
  </div>
  <div class="item" style="left:86px;top:216px;width:272px">
    <h3>Bloomin’ Cactus</h3>
    <p><span class="line">A sweet, colossal onion sliced to bloom, battered and</span>
    <span class="line">fried to a golden brown. Served with Cactus Sauce.</span>
    <span class="price solo">6.99</span></p>
  </div>
  <div class="item" style="left:86px;top:285px;width:272px">
    <h3>Italian Nachos</h3>
    <p><span class="line">Crispy wonton chips, Italian sausage, black olives,</span>
    <span class="line">jalapenos, sliced peperoncinis, diced tomatoes, drizzled</span>
    <span class="line">with rich Alfredo sauce and topped with melted</span>
    <span class="line"><span>mozzarella.</span><span class="price">9.99</span></span></p>
  </div>

  <div class="item" style="left:383px;top:146px;width:274px">
    <h3>Fried Pickles</h3>
    <p><span class="line">Our version of a Southern specialty. Dill pickle slices</span>
    <span class="line">lightly hand breaded and golden fried. Served with</span>
    <span class="line"><span>homemade ranch dressing.</span><span class="price">4.99</span></span></p>
  </div>
  <div class="item" style="left:383px;top:216px;width:274px">
    <h3>Buffalo Wings</h3>
    <p><span class="line">Cool ’em down with our homemade bleu cheese</span>
    <span class="line"><span>dressing.</span><span class="price">6.99</span></span></p>
  </div>
  <div class="item" style="left:383px;top:285px;width:274px">
    <h3>Loaded Cheese Fries</h3>
    <p><span class="line">We mix in some bacon and sautéed onion, then melted</span>
    <span class="line"><span>cheddar cheese over the top.</span><span class="price">7.99</span></span></p>
  </div>

  <!-- Salads -->
  <div class="rule" style="left:68px;top:386px;width:622px"></div>
  <h2 class="section-title" style="top:390px">SALADS</h2>
  <p class="section-note" style="top:431px">These garden fresh salads are served with our freshly baked Thornvales’ bread or an apple.</p>
  <div class="rule" style="left:68px;top:454px;width:622px"></div>

  <div class="item" style="left:101px;top:477px;width:275px">
    <h3>Caesar Salad</h3>
    <p><span class="line">Tender, charbroiled chicken breast served on a bed of</span>
    <span class="line">fresh Romaine lettuce, tossed with Caesar dressing,</span>
    <span class="line">parmesan cheese, and croutons.</span></p>
  </div>
  <div class="options" style="left:267px;top:538px">
    <div><span class="label">Chicken</span><span class="price">9.49</span></div>
    <div><span class="label">Salmon</span><span class="price">12.49</span></div>
  </div>
  <div class="item" style="left:101px;top:567px;width:275px">
    <h3>Fiesta Salad</h3>
    <p><span class="line">Your choice of fajita beef or chicken with lettuce,</span>
    <span class="line">shredded cheddar cheese, tomatoes, onions and</span>
    <span class="line">croutons. Served with a side of pico de gallo.</span></p>
  </div>
  <div class="options" style="left:267px;top:628px">
    <div><span class="label">Beef</span><span class="price">9.99</span></div>
    <div><span class="label">Chicken</span><span class="price">9.49</span></div>
  </div>
  <div class="item" style="left:101px;top:656px;width:280px">
    <h3>Rancher’s Salad</h3>
    <p><span class="line">Seasoned strips of sautéed beef with grilled onions and</span>
    <span class="line">mushrooms on a cool bed of greens. Sprinkled with</span>
    <span class="line" style="width:275px"><span>diced tomatoes and bleu cheese crumbles.</span><span class="price">10.99</span></span></p>
  </div>
  <div class="item" style="left:101px;top:731px;width:280px">
    <h3>Cobb Salad</h3>
    <p><span class="line">Tender strips of chicken breast on a bed of fresh greens,</span>
    <span class="line">tomato, onion, cheese, slices of hard-boiled boiled egg,</span>
    <span class="line">diced bacon, crumbled bleu cheese, croutons and your</span>
    <span class="line" style="width:275px"><span>choice of dressing.</span><span class="price">10.49</span></span></p>
  </div>

  <div class="item" style="left:398px;top:477px;width:271px">
    <h3>Chicken Tender Salad</h3>
    <p><span class="line">Crispy chicken tenders served hot over a bed of fresh</span>
    <span class="line">lettuce, cheddar cheese, tomatoes, onions, and your</span>
    <span class="line"><span>choice of dressing.</span><span class="price">9.49</span></span></p>
  </div>
  <div class="item" style="left:398px;top:549px;width:271px">
    <h3>Apple Orchard Salad</h3>
    <p><span class="line">Sliced grilled chicken breast, fresh mixed greens, with</span>
    <span class="line">cranberries, chopped walnuts, red onions and bleu</span>
    <span class="line">cheese crumbles. Garnished with dried apple chips.</span>
    <span class="price solo">11.49</span></p>
  </div>
  <div class="item" style="left:396px;top:624px;width:286px">
    <h3>Chef Salad</h3>
    <p><span class="line">Classic combination of sliced turkey, ham, Swiss cheese,</span>
    <span class="line">and cheddar cheese mixed with salad greens, onions,</span>
    <span class="line" style="width:281px"><span>tomatoes, topped with a sliced hard-boiled egg.</span><span class="price">10.49</span></span></p>
  </div>
  <div class="item" style="left:396px;top:700px;width:281px">
    <h3>Greek Salad</h3>
    <p><span class="line">An authentic Mediterranean salad of tender chicken,</span>
    <span class="line">juicy tomatoes, sliced red onion, crumbled feta cheese,</span>
    <span class="line" style="width:277px"><span>and black olives. Served with Greek dressing.</span><span class="price">10.49</span></span></p>
  </div>

  <!-- Soups -->
  <div class="rule" style="left:60px;top:832px;width:622px"></div>
  <h2 class="section-title" style="top:838px">SOUPS</h2>
  <p class="section-note" style="top:880px">All selections homemade in our kitchen and available every day.</p>
  <div class="rule" style="left:60px;top:900px;width:622px"></div>

  <div class="item" style="left:101px;top:926px;width:290px">
    <h3>Chicken Enchilada Soup</h3>
    <p><span class="line">Topped with pico de gallo and tortilla strips.</span></p>
  </div>
  <div class="item" style="left:101px;top:968px;width:290px">
    <h3>French Onion</h3>
    <p><span class="line">Sweet caramelized onions in a savory broth. Crowned</span>
    <span class="line">with baked mozzarella.</span></p>
  </div>
  <div class="options" style="left:267px;top:1029px">
    <div><span class="label">Cup</span><span class="price">2.99</span></div>
    <div><span class="label">Bowl</span><span class="price">5.49</span></div>
  </div>
</div>
</body>
</html>
```